Website for sailing around the world

I'm planning to sail around the world with a sailing katamaran in about 8 jears. Together with my best friend we want to be "on tour" for at least 10 jears (or more). I have no idea about webdesign. It should be a wordpress site. I would like to have some links like: "about us", "about the boat", if possible i woul like to show: where is the boat rigt now, links to facebook, twitter, google+ ect., an archive to list all our daily- weekly blog articles which we will send from the boat to the website...
I already tried to build a wordpress website, but its not good enough 😩.
The boat name is: VorraBay
Maby you want to see the website i try to build by myself: vorrabay.example-blogs.net

Until i am collecting money for this trip i want to "play" with this website during my sailing-holidays (getting better in uploading block-articles, getting better in "using" my webste).

Target Market(s)

Webdesign
Sailing Blog

Industry/Entity Type

Tour

Colors

Designer to choose colors to be used in the design.

Requirements
Must have
• Should be nice to view.
• Must be easy to handle for "non it person" (me)
• Liks to facebook, twitter, google+
• People who follow us on wordpress should be informed if we post a new blog article...
Nice to have
• Please see my first adventure on wordpress:
• Vorrabay.example-blogs.net
• (Here i tried to build a website by my own, but i am not good in this...
• Maby someone can build an account on fb,twitter, google+ (something with "vorraBay" in the account-name...

```html
<!DOCTYPE html>
<html lang="en">
<head>
<meta charset="utf-8">
<title>VorraBay – Sailing Around the World</title>
<link rel="stylesheet" href="https://fonts.googleapis.com/css2?family=Oswald:wght@600&family=Quicksand:wght@600;700&family=Roboto:wght@400;500;700&display=swap">
<style>
  :root{
    --orange:#e8650f;
    --ink:#333333;
    --text:#6b6b6b;
    --muted:#8a8a8a;
    --light:#f3f3f3;
    --white:#ffffff;
    --dark:#1f1f1f;
  }
  *{margin:0;padding:0;box-sizing:border-box}
  html,body{width:1200px;height:2711px;overflow:hidden;background:var(--white)}
  body{position:relative;font-family:'Roboto',sans-serif;color:var(--ink)}
  .section{position:absolute;left:0;width:1200px}

  /* header */
  .site-header{top:0;height:68px;background:var(--orange)}
  .brand{position:absolute;left:49px;top:12px;font-weight:700;font-size:34px;color:var(--white)}
  .main-nav{position:absolute;left:288px;top:25px;display:flex;font-size:14px;color:var(--white);letter-spacing:.3px}
  .main-nav span{margin-right:23px}
  .main-nav span:last-child{margin-right:0}
  .main-nav .active{color:#1f1f1f}
  .social-top{position:absolute;right:52px;top:24px;display:flex;gap:20px}
  .social-top i{display:block;width:18px;height:18px;border-radius:50%;background:var(--white)}

  /* hero */
  .hero{top:68px;height:505px;background:linear-gradient(100deg,#2f4a66 0%,#4a6b85 35%,#6e6a66 60%,#3b3a3d 100%)}
  .hero-title{position:absolute;left:49px;top:108px;font-family:'Oswald',sans-serif;font-weight:600;font-size:60px;color:var(--white);letter-spacing:.5px;line-height:1}
  .hero-lead{position:absolute;left:49px;top:184px;width:740px;font-family:'Quicksand',sans-serif;font-weight:700;font-size:33px;line-height:38px;color:var(--white)}
  .hero-btn{position:absolute;left:49px;top:329px;width:175px;height:58px;border:2px solid var(--white);color:var(--white);font-family:'Quicksand',sans-serif;font-weight:700;font-size:24px;display:flex;align-items:center;justify-content:center}

  /* section titles */
  .section-title{position:absolute;left:0;width:1200px;text-align:center;font-family:'Quicksand',sans-serif;font-weight:700;font-size:32px;color:var(--orange);letter-spacing:.5px}
  .divider{position:absolute;left:528px;width:144px;height:26px}

  /* welcome */
  .welcome{top:573px;height:484px;background:var(--white)}
  .compass{position:absolute;left:96px;top:137px;width:296px;height:296px;background:linear-gradient(135deg,#c9ced4,#5a7fb5)}
  .welcome-rule{position:absolute;left:435px;top:141px;width:2px;height:298px;background:#7a7a7a}
  .welcome-heading{position:absolute;left:464px;top:130px;width:700px;font-family:'Quicksand',sans-serif;font-weight:700;font-size:31px;line-height:38px;color:var(--orange)}
  .welcome-text{position:absolute;left:464px;top:211px;width:690px;font-size:16.5px;line-height:26.6px;color:var(--text)}
  .btn-solid{position:absolute;background:var(--orange);color:var(--white);font-weight:500;display:flex;align-items:center;justify-content:center}
  .read-more{left:457px;top:390px;width:116px;height:43px;font-size:15px}

  /* boats */
  .boats{top:1057px;height:723px;background:var(--light)}
  .boat-grid{position:absolute;left:49px;top:128px;width:1104px;height:548px;display:grid;grid-template-columns:1fr 1fr;grid-template-rows:1fr 1fr}
  .boat-tile{position:relative;overflow:hidden}
  .boat-tile .photo{position:absolute;inset:0}
  .tile-a .photo{background:linear-gradient(135deg,#7d8a94,#3f5363 60%,#2c3d4b)}
  .tile-b .photo{background:linear-gradient(135deg,#5e7283,#394a58 60%,#26333e)}
  .tile-c .photo{background:linear-gradient(135deg,#8895a0,#45596a 60%,#2a3a48)}
  .tile-d .photo{background:linear-gradient(135deg,#6f7e8c,#3c4d5d 60%,#283642)}
  .boat-tile .shade{position:absolute;inset:0;background:rgba(15,25,35,.35)}
  .boat-name{position:absolute;left:0;right:0;top:74px;text-align:center;font-family:'Quicksand',sans-serif;font-weight:700;font-size:32px;color:var(--white)}
  .boat-line{position:absolute;left:146px;width:260px;top:114px;height:2px;background:var(--white)}
  .boat-text{position:absolute;left:66px;width:420px;top:132px;text-align:center;font-size:13.5px;line-height:19px;color:var(--white)}
  .view-btn{position:absolute;left:217px;top:188px;width:118px;height:33px;border:1px solid var(--white);color:var(--white);font-size:11.5px;display:flex;align-items:center;justify-content:center}

  /* blog */
  .blog{top:1780px;height:605px;background:var(--white)}
  .blog-cards{position:absolute;left:49px;top:126px;width:1104px;display:flex;gap:28px}
  .blog-card{width:349px;height:376px;background:var(--white);box-shadow:0 4px 14px rgba(0,0,0,.14)}
  .blog-card .photo{height:238px}
  .card-1 .photo{background:linear-gradient(160deg,#9fb3c6,#5d6f7e 60%,#3e4a55)}
  .card-2 .photo{background:linear-gradient(160deg,#c5d2de,#8ea0b1 60%,#5f6e7c)}
  .card-3 .photo{background:linear-gradient(160deg,#7fb3d3,#3f98b8 55%,#d7e3ea)}
  .post-meta{margin-top:26px;text-align:center;font-size:13px;color:var(--ink)}
  .card-1 .post-meta .date{color:var(--orange)}
  .post-title{margin:12px auto 0;width:300px;text-align:center;font-size:19px;line-height:23px;font-weight:400;color:var(--ink)}
  .card-1 .post-title{color:var(--orange);font-weight:500}
  .view-more{left:544px;top:524px;width:119px;height:36px;font-size:13px}

  /* footer */
  .site-footer{top:2385px;height:271px;background:var(--light)}
  .foot-col{position:absolute;top:50px}
  .foot-col h4{font-weight:500;font-size:17px;color:var(--ink);padding-bottom:8px;border-bottom:1px solid #c9c9c9;display:inline-block}
  .foot-nav{left:49px}
  .foot-nav h4{width:108px}
  .foot-nav ul{list-style:none;margin-top:10px}
  .foot-nav li{font-size:13px;color:var(--muted);line-height:28.5px}
  .foot-nav li.current{color:var(--orange)}
  .foot-news{left:392px;width:300px}
  .foot-news h4{width:296px}
  .foot-news p{margin-top:12px;font-size:13px;line-height:20px;color:var(--muted)}
  .subscribe{margin-top:16px;display:flex;height:30px}
  .subscribe .field{width:166px;background:#2a2a2a;color:#bbb;font-size:11.5px;display:flex;align-items:center;padding-left:42px;position:relative}
  .subscribe .field svg{position:absolute;left:8px;top:8px}
  .subscribe .go{width:94px;background:var(--orange);color:var(--white);font-size:12px;font-style:italic;font-weight:700;display:flex;align-items:center;justify-content:center}
  .foot-contact{left:938px;width:220px}
  .foot-contact h4{width:108px}
  .contact-row{display:flex;gap:10px;margin-top:14px;font-size:12.5px;line-height:17px;color:var(--muted)}
  .contact-row svg{flex:none;margin-top:2px}
  .social-foot{display:flex;gap:22px;margin-top:16px}
  .social-foot i{display:block;width:14px;height:14px;border-radius:50%;background:var(--ink)}
  .social-foot i:first-child{background:var(--orange)}
  .bottom-bar{top:2656px;height:55px;background:var(--dark);color:var(--white);font-size:14px;text-align:center;line-height:55px}
</style>
</head>
<body>

<header class="section site-header">
  <div class="brand">VorraBay</div>
  <nav class="main-nav">
    <span class="active">HOME</span><span>/</span>
    <span>ABOUT US</span><span>/</span>
    <span>MARTEN</span><span>/</span>
    <span>JORIK</span><span>/</span>
    <span>THE BOAT</span><span>/</span>
    <span>CONTACT</span>
  </nav>
  <div class="social-top" aria-label="Social links"><i></i><i></i><i></i><i></i><i></i></div>
</header>

<section class="section hero" role="img" aria-label="Photo of a smiling couple steering a motorboat at sunset">
  <h1 class="hero-title">BUY A BOAT FROM A DEALER</h1>
  <p class="hero-lead">Private sellers and auctioneers cannot offer financing deals that the dealers ships can. Buy a boat from a dealer.</p>
  <div class="hero-btn">Sailing Boat</div>
</section>

<section class="section welcome">
  <h2 class="section-title" style="top:40px">WELCOME TO VORRABAY</h2>
  <svg class="divider" style="top:85px" viewBox="0 0 144 26"><line x1="0" y1="11" x2="144" y2="11" stroke="#333" stroke-width="1.5"/><g fill="none" stroke="#333" stroke-width="1.8"><circle cx="72" cy="3.5" r="2.5"/><line x1="72" y1="6" x2="72" y2="23"/><line x1="66" y1="10" x2="78" y2="10"/><path d="M63 16 Q66 23 72 23 Q78 23 81 16"/></g></svg>
  <div class="compass" role="img" aria-label="Illustration of a compass"></div>
  <div class="welcome-rule"></div>
  <h3 class="welcome-heading">OFFERING A WIDE SELECTION OF LUXURY MOTOR &amp; SAILING YACHTS</h3>
  <p class="welcome-text">Lorem ipsum dolor sit amet, consectetur adipiscing elit. Curabitur est nulla, faucibus ut sed, ultrices ac elit. Mauris arcu sem, auctor et facilisis non, commodo et magna. Duis eros urus, molestie vel mi vel, rutrum gravida sapien. In tincidunt nisi sit amet eros faucibus dignissim. Praesent purus velit, malesuada et eros in, vehicula vestibulum nisl. Curabitur leo massainia ac tristique in, sodales at mauris. Interdum et malesuada fames ac ante ipsum primis inus. Fusce at lobortis velit. Quisque lorem lacus, fermentum eu hendrerit id,</p>
  <div class="btn-solid read-more">Read More</div>
</section>

<section class="section boats">
  <h2 class="section-title" style="top:43px">SAILING BOATS</h2>
  <svg class="divider" style="top:88px" viewBox="0 0 144 26"><line x1="0" y1="11" x2="144" y2="11" stroke="#333" stroke-width="1.5"/><g fill="none" stroke="#333" stroke-width="1.8"><circle cx="72" cy="3.5" r="2.5"/><line x1="72" y1="6" x2="72" y2="23"/><line x1="66" y1="10" x2="78" y2="10"/><path d="M63 16 Q66 23 72 23 Q78 23 81 16"/></g></svg>
  <div class="boat-grid">
    <article class="boat-tile tile-a">
      <div class="photo" role="img" aria-label="Photo of a man on the deck of a luxury yacht"></div><div class="shade"></div>
      <h3 class="boat-name">LUXURY YACHTS</h3><div class="boat-line"></div>
      <p class="boat-text">Lorem ipsum dolor sit amet, consectetur adipiscing elit. Sed vestibulum sed libero in suscipit. In vitae turpis</p>
      <div class="view-btn">VIEW MORE</div>
    </article>
    <article class="boat-tile tile-b">
      <div class="photo" role="img" aria-label="Photo of a man aboard a motor boat"></div><div class="shade"></div>
      <h3 class="boat-name">MOTOR BOATS</h3><div class="boat-line"></div>
      <p class="boat-text">Lorem ipsum dolor sit amet, consectetur adipiscing elit. Sed vestibulum sed libero in suscipit. In vitae turpis</p>
      <div class="view-btn">VIEW MORE</div>
    </article>
    <article class="boat-tile tile-c">
      <div class="photo" role="img" aria-label="Photo of a man standing on a catamaran deck"></div><div class="shade"></div>
      <h3 class="boat-name">CATAMARANS</h3><div class="boat-line"></div>
      <p class="boat-text">Lorem ipsum dolor sit amet, consectetur adipiscing elit. Sed vestibulum sed libero in suscipit. In vitae turpis</p>
      <div class="view-btn">VIEW MORE</div>
    </article>
    <article class="boat-tile tile-d">
      <div class="photo" role="img" aria-label="Photo of a sailing boat in a city harbour"></div><div class="shade"></div>
      <h3 class="boat-name">SAILING BOATS</h3><div class="boat-line"></div>
      <p class="boat-text">Lorem ipsum dolor sit amet, consectetur adipiscing elit. Sed vestibulum sed libero in suscipit. In vitae turpis</p>
      <div class="view-btn">VIEW MORE</div>
    </article>
  </div>
</section>

<section class="section blog">
  <h2 class="section-title" style="top:40px">LATEST BLOG</h2>
  <svg class="divider" style="top:85px" viewBox="0 0 144 26"><line x1="0" y1="11" x2="144" y2="11" stroke="#333" stroke-width="1.5"/><g fill="none" stroke="#333" stroke-width="1.8"><circle cx="72" cy="3.5" r="2.5"/><line x1="72" y1="6" x2="72" y2="23"/><line x1="66" y1="10" x2="78" y2="10"/><path d="M63 16 Q66 23 72 23 Q78 23 81 16"/></g></svg>
  <div class="blog-cards">
    <article class="blog-card card-1">
      <div class="photo" role="img" aria-label="Photo of a sailor at the helm wearing a life jacket"></div>
      <p class="post-meta"><span class="date">June 8, 2017</span> &nbsp;|&nbsp; 2 comments</p>
      <h3 class="post-title">Curabitur est nulla faucibusut mollis sedultrices acelit.</h3>
    </article>
    <article class="blog-card card-2">
      <div class="photo" role="img" aria-label="Photo of a sailor steering a yacht under grey sky"></div>
      <p class="post-meta"><span class="date">June 7, 2017</span> &nbsp;|&nbsp; 3 comments</p>
      <h3 class="post-title">vehicula vestibulum nislurabi leo massaconvallis ac mollis</h3>
    </article>
    <article class="blog-card card-3">
      <div class="photo" role="img" aria-label="Photo of a white catamaran on turquoise water"></div>
      <p class="post-meta"><span class="date">June 6, 2017</span> &nbsp;|&nbsp; 5 comments</p>
      <h3 class="post-title">lacinia ac tristique in sodales at maurislectus id vestibulum eli</h3>
    </article>
  </div>
  <div class="btn-solid view-more">VIEW MORE</div>
</section>

<footer class="section site-footer">
  <div class="foot-col foot-nav">
    <h4>Nevigation</h4>
    <ul>
      <li class="current">Home</li><li>About Us</li><li>Marten</li><li>Jorik</li><li>The Boat</li><li>Contact</li>
    </ul>
  </div>
  <div class="foot-col foot-news">
    <h4>VorraBay Solutions Newsletters</h4>
    <p>Subscribe to keep up to date with VorraBay news, updates, roster additions and just plain old good stuff!!!!</p>
    <div class="subscribe">
      <div class="field"><svg width="24" height="14" viewBox="0 0 24 14"><rect x="1" y="1" width="22" height="12" fill="none" stroke="#999" stroke-width="1.5"/><path d="M1 1 L12 8 L23 1" fill="none" stroke="#999" stroke-width="1.5"/></svg>your@email.com</div>
      <div class="go">Subscribe</div>
    </div>
  </div>
  <div class="foot-col foot-contact">
    <h4>Get In Touch</h4>
    <div class="contact-row"><svg width="14" height="18" viewBox="0 0 14 18"><path d="M7 1 C3.5 1 1 3.5 1 7 C1 11 7 17 7 17 C7 17 13 11 13 7 C13 3.5 10.5 1 7 1Z" fill="#e8650f"/><circle cx="7" cy="7" r="2.3" fill="#f3f3f3"/></svg><span>VorraBay<br>5102 Lorem ipsum dolor sit amet, maximus bibendum 77845</span></div>
    <div class="contact-row"><svg width="16" height="16" viewBox="0 0 16 16"><path d="M3 1 L6 1 L7 5 L5 6.5 C6 9 7 10 9.5 11 L11 9 L15 10 L15 13 C15 14 14 15 13 15 C6 15 1 10 1 3 C1 2 2 1 3 1Z" fill="#e8650f"/></svg><span>123-456-7890</span></div>
    <div class="contact-row"><svg width="16" height="12" viewBox="0 0 16 12"><rect width="16" height="12" fill="#e8650f"/><path d="M0 0 L8 7 L16 0" fill="none" stroke="#f3f3f3" stroke-width="1.3"/></svg><span>info@vorrabay.example</span></div>
    <div class="social-foot" aria-label="Social links"><i></i><i></i><i></i><i></i><i></i><i></i></div>
  </div>
</footer>

<div class="section bottom-bar">© 2017 VorraBay &nbsp;| All Rights Reserved.</div>

</body>
</html>
```